Need a banner made for my LinkedIn Profile

We are a sell side advisor and we need to update our LinkedIn banner
Amber Ridge offers two services:
1. Sell Side Advisory
2. And through our TetherMark program, Exit Readiness

Target Market(s)

Business owners, Private Equity Firms

Industry/Entity Type

Mergers and Acquisitions

Logo Text

Sell-Side Advisory Exit-Readiness

Font styles to use
Other font styles liked:
• Match logo fonts

Colors

Designer to choose colors to be used in the design.

Requirements
Must have
• Use the colors on the Amber Ridge Logo-All white background, use both logos

```html
<!DOCTYPE html>
<html lang="en">
<head>
<meta charset="utf-8">
<title>Amber Ridge Capital – LinkedIn Banner</title>
<link href="https://fonts.googleapis.com/css2?family=Poppins:wght@500;600&display=swap" rel="stylesheet">
<style>
  :root {
    --page-bg: #fdfdfd;
    --banner-bg: #0f1316;
    --text-light: #ffffff;
    --wave-light: rgba(233, 238, 240, 0.16);
    --wave-teal: rgba(38, 138, 157, 0.22);
    --accent-teal: #268a9d;
  }
  html, body {
    margin: 0;
    padding: 0;
    width: 1200px;
    height: 1200px;
    overflow: hidden;
    background: var(--page-bg);
  }
  .canvas {
    position: relative;
    width: 1200px;
    height: 1200px;
  }
  .banner {
    position: absolute;
    left: 109px;
    top: 516px;
    width: 982px;
    height: 166px;
    background: var(--banner-bg);
    overflow: hidden;
    font-family: "Poppins", sans-serif;
  }
  .banner__wave-area {
    position: absolute;
    left: 0;
    right: 0;
    top: 58px;
    bottom: 0;
    background:
      radial-gradient(ellipse 40% 60% at 28% 55%, var(--wave-light), transparent 70%),
      radial-gradient(ellipse 35% 55% at 82% 45%, var(--wave-light), transparent 70%),
      radial-gradient(ellipse 30% 45% at 12% 75%, var(--wave-teal), transparent 70%),
      radial-gradient(ellipse 25% 40% at 95% 50%, var(--wave-teal), transparent 70%);
  }
  .services {
    position: absolute;
    left: 166px;
    top: 16px;
    margin: 0;
    padding: 0;
    list-style: none;
    color: var(--text-light);
    font-weight: 500;
    font-size: 13.5px;
    line-height: 17px;
    letter-spacing: 0.1px;
  }
  .brand {
    position: absolute;
    left: 593px;
    top: 20px;
    display: flex;
    align-items: center;
    gap: 10px;
  }
  .brand__mark {
    width: 34px;
    height: 34px;
    border-radius: 50%;
    background: var(--accent-teal);
    flex: none;
  }
  .brand__name {
    margin: 0;
    color: var(--text-light);
    font-weight: 600;
    font-size: 18.5px;
    letter-spacing: -0.3px;
    white-space: nowrap;
  }
</style>
</head>
<body>
<div class="canvas">
  <section class="banner" aria-label="Amber Ridge Capital LinkedIn banner">
    <div class="banner__wave-area" role="img" aria-label="Decorative flowing white and teal wave lines across the lower banner"></div>

    <ul class="services">
      <li>Sell-Side Advisory</li>
      <li>Exit-Readiness</li>
    </ul>

    <div class="brand">
      <span class="brand__mark" aria-hidden="true"></span>
      <p class="brand__name">Amber Ridge Capital</p>
    </div>
  </section>
</div>
</body>
</html>
```